Business Card for Sugared Soiree

I have a logo for my candy buffet business, and need a business card designed using that logo. Sugared Soiree designs and builds beautiful and delicious candy and dessert tables for all kinds of events. The card should be simple, modern, graphic, colorful, and use the Sugared Soiree Logo.

Target Market(s)

The target market is people hosting major parties and events. This includes brides getting married, parents hosting birthday parties/Sweet Sixteen/Bar Mitzvah/quinceanera parties, and companies hosting corporate events.

Industry/Entity Type

Business

Requirements
Must have
• The business card must have the logo, with or without the tag line.

The following information must be on the card:

Dana Whitfield
CEO & Candy Stylist
614.392.5071
dana@sugaredsoiree-example.com
Nice to have
• I like the idea of having multiple colors of the same design so that several people receiving cards will each receive a different color. Perhaps 3-5 colors or variations on a basic card design.

```html
<!DOCTYPE html>
<html lang="en">
<head>
<meta charset="utf-8">
<title>Sugared Soiree — Business Card</title>
<link href="https://fonts.googleapis.com/css2?family=Poppins:wght@300;600&display=swap" rel="stylesheet">
<style>
  :root {
    --page: #ffffff;
    --ink: #111111;
    --card-edge: #222222;
    --magenta: #ec0c8c;
    --tag: #f7b3d8;
    --yellow: #f5e23a;
    --cyan: #4fc3ee;
    --green: #3aa35a;
    --blush: #f5a6cf;
  }
  html, body {
    margin: 0;
    padding: 0;
    width: 1200px;
    height: 669px;
    overflow: hidden;
    background: var(--page);
    font-family: "Poppins", sans-serif;
  }
  .canvas {
    position: relative;
    width: 1200px;
    height: 669px;
  }
  .card {
    position: absolute;
    top: 208px;
    width: 454px;
    height: 285px;
    border: 1px solid var(--card-edge);
  }
  .card--front {
    left: 105px;
    background: var(--page);
    display: flex;
    flex-direction: column;
    align-items: center;
    justify-content: center;
  }
  .brand-dot {
    width: 44px;
    height: 44px;
    border-radius: 50%;
    background: var(--magenta);
    margin-bottom: 14px;
  }
  .brand-name {
    margin: 0;
    font-weight: 300;
    font-size: 48px;
    letter-spacing: -0.5px;
    line-height: 1;
    color: var(--ink);
  }
  .card--back {
    left: 587px;
    background: var(--magenta);
  }
  .tagline {
    position: absolute;
    top: 20px;
    left: 34px;
    right: 34px;
    display: flex;
    align-items: center;
    gap: 10px;
    font-weight: 300;
    font-size: 11px;
    color: var(--tag);
    white-space: nowrap;
  }
  .tagline::before,
  .tagline::after {
    content: "";
    flex: 1;
    height: 1px;
    background: var(--tag);
    opacity: 0.8;
  }
  .contact {
    position: absolute;
    left: 22px;
    top: 160px;
    margin: 0;
    font-style: normal;
    font-weight: 300;
    font-size: 19px;
    line-height: 23px;
  }
  .contact span { display: block; }
  .contact__name { color: var(--yellow); }
  .contact__name strong { font-weight: 600; }
  .contact__role { color: var(--cyan); }
  .contact__phone { color: var(--green); }
  .contact__email { color: var(--blush); }
</style>
</head>
<body>
<main class="canvas">
  <section class="card card--front" aria-label="Card front">
    <div class="brand-dot"></div>
    <h1 class="brand-name">sugaredsoiree</h1>
  </section>

  <section class="card card--back" aria-label="Card back">
    <div class="tagline">the best part of the party</div>
    <address class="contact">
      <span class="contact__name">dana <strong>whitfield</strong></span>
      <span class="contact__role">ceo &amp; candy stylist</span>
      <span class="contact__phone">614 392 5071</span>
      <span class="contact__email">dana@sugaredsoiree-example.com</span>
    </address>
  </section>
</main>
</body>
</html>
```